" Ofereceremos descontos em consultas e exames, para contratar o plano mensal (ou anual), bem como teremos parceria com segmentos de serviços em bem estar e qualidade de vida (farmácias, laboratórios, nutrição, etc) "

```html
<!DOCTYPE html>
<html lang="pt-BR">
<head>
<meta charset="UTF-8">
<title>Envelope Carta – NovaVida Benefícios</title>
<link href="https://fonts.googleapis.com/css2?family=Montserrat:wght@400;500;600;700&display=swap" rel="stylesheet">
<style>
  :root {
    --bg: #e4e4e6;
    --purple: #7a1f86;
    --teal: #22b3a3;
    --white: #ffffff;
    --label: #6d6d72;
  }
  * { margin: 0; padding: 0; box-sizing: border-box; }
  html, body { width: 1200px; height: 1200px; overflow: hidden; }
  body {
    background: var(--bg);
    font-family: "Montserrat", sans-serif;
    position: relative;
  }
  .sheet-label {
    position: absolute;
    top: 84px; right: 156px;
    font-size: 34px; font-weight: 500; letter-spacing: 1px;
    color: var(--label);
  }
  .envelope {
    position: absolute;
    left: 168px; width: 960px;
    box-shadow: 0 10px 24px rgba(0,0,0,.18);
    overflow: hidden;
  }
  .envelope-back {
    top: 180px; height: 456px;
    background: var(--purple);
  }
  .envelope-back .flap { position: absolute; inset: 0; }
  .contact-list {
    position: absolute;
    left: 46px; top: 262px;
    list-style: none;
    color: var(--white);
    font-size: 17px; line-height: 1.25;
  }
  .contact-list li {
    display: flex; align-items: flex-start; gap: 12px;
    margin-bottom: 18px;
  }
  .contact-list svg, .contact-list .icon-space { width: 16px; height: 16px; flex: none; margin-top: 2px; }
  .brand {
    position: absolute;
    display: flex; align-items: center; gap: 12px;
    font-weight: 700; font-size: 34px;
    white-space: nowrap;
  }
  .brand .mark { width: 20px; height: 20px; flex: none; }
  .envelope-back .brand { right: 52px; top: 292px; color: var(--white); }
  .envelope-back .brand .mark { background: var(--white); }
  .envelope-front {
    top: 667px; height: 461px;
    background: var(--white);
  }
  .envelope-front .bottom-band {
    position: absolute; left: 0; right: 0; bottom: 0;
    height: 18px; background: var(--teal);
  }
  .envelope-front .brand { left: 56px; top: 196px; color: var(--purple); }
  .envelope-front .brand .mark { background: var(--purple); }
</style>
</head>
<body>
  <div class="sheet-label">ENVELOPE CARTA</div>

  <section class="envelope envelope-back">
    <svg class="flap" viewBox="0 0 960 456" preserveAspectRatio="none">
      <path d="M0,0 H960 V14 C820,22 560,60 360,72 C260,78 200,80 168,108 C150,124 120,138 0,138 Z" fill="var(--teal)"/>
    </svg>

    <ul class="contact-list">
      <li>
        <svg viewBox="0 0 24 24"><path fill="#fff" d="M6.6 10.8a15 15 0 0 0 6.6 6.6l2.2-2.2c.3-.3.7-.4 1-.2 1.1.4 2.3.6 3.6.6.6 0 1 .4 1 1V20c0 .6-.4 1-1 1A17 17 0 0 1 3 4c0-.6.4-1 1-1h3.5c.6 0 1 .4 1 1 0 1.3.2 2.5.6 3.6.1.3 0 .7-.2 1z"/></svg>
        <span>(90) 98000-12345</span>
      </li>
      <li>
        <svg viewBox="0 0 24 24"><path fill="#fff" d="M12 2a7 7 0 0 0-7 7c0 5.2 7 13 7 13s7-7.8 7-13a7 7 0 0 0-7-7zm0 9.5A2.5 2.5 0 1 1 12 6.5a2.5 2.5 0 0 1 0 5z"/></svg>
        <span>Rua das Acácias, 18 - Centro<br>Cidade/UF - CEP: 00000-111</span>
      </li>
      <li>
        <svg viewBox="0 0 24 24"><path fill="#fff" d="M3 5h18v14H3z"/><path d="M3 5l9 7 9-7" fill="none" stroke="#7a1f86" stroke-width="2"/></svg>
        <span>contato@novavida.com.br</span>
      </li>
      <li>
        <span class="icon-space"></span>
        <span>@novavida</span>
      </li>
    </ul>

    <div class="brand"><span class="mark"></span>NovaVida Benefícios</div>
  </section>

  <section class="envelope envelope-front">
    <div class="brand"><span class="mark"></span>NovaVida Benefícios</div>
    <div class="bottom-band"></div>
  </section>
</body>
</html>
```